Facebook & Instagram Ads for Quillbright, the world's first device to improve memory throu...

About Us
Quillbright® is a revolutionary bedside device that improves memory while you sleep. Backed by groundbreaking clinical research from the Harlow Ridge Institute of Sciences, our device uses gentle, rotating scents to enhance memory and brian fog naturally. With zero pills, zero side effects, and zero effort, Quillbright offers a new path to better memory. www.quillbright-example.com

The Challenge
We are looking for bold, imaginative, and highly shareable static and GIF ad designs for Facebook and Instagram. This isn’t just another health device—it’s a category-defining product. Your job is to help us stop the scroll with creative ad concepts that communicate the elegance, science, and life-changing benefits of Quillbright.

What We’re Looking For
Format: Static images + short GIF animations (3–8 seconds)
Platforms: Facebook feed, Instagram feed, Instagram Reels
Style: Modern, aspirational, elegant, clean — with a premium feel
Target Audience: Affluent men and women, ages 50+, health-conscious, looking for ways to support memory and brain health and people concerned or worried that they’re losing their memory and aren’t thinking as quickly or crisply as they want,

Creative Direction
Show Quillbright as a premium lifestyle product (not medical or clinical in look).
Think high-end wellness meets cutting-edge science.
Use strong visual hooks: elegant bedside setups, active seniors, subtle cues to scents and sleep, calming colors.
Text overlays should be minimal and impactful.

Tone of Voice (for ad copy in the designs)
Aspirational yet credible
Warm, trustworthy, and empowering
Avoid fear tactics or overpromising

Approved Messaging
✅ Quillbright improves memory while you sleep
✅ Clinically backed & drug-free
✅ Simple, effortless nightly use
✅ No RX, no side effects
✅ Elegant bedside design
✅ Improves your mood
✅ Feel Younger
✅ Developed by a top 2% scientist in the world (Pellington School of Medicine Study)
✅ 226% memory improvement in seniors
✅ 300% memory improvement in dementia patients

Do NOT Say
❌ Cures Alzheimer’s or dementia
❌ Guaranteed results
❌ Any medical claims beyond memory improvement and cognition support

Deliverables
2+ static ad concepts (1080x1080 + 1080x1920 formats)
1+ short GIF ad concepts (3–8 seconds, loopable)
Layered source files (PSD/AI) preferred

What We’ll Provide You
Our website for reference: www.quillbright-example.com
Brand guidelines (logo, colors, fonts)
Approved copy lines and scientific references
Device imagery (with logo placement guidelines)

What We Want to See in Your Work
Unique and scroll-stopping ad ideas (not cookie-cutter templates)
Clever ways to communicate memory improvement + science through visuals
A mix of direct product focus AND lifestyle storytelling

Inspiration
Think of Vartuna, Lumet Band, or Korvel level of sleekness—premium, modern, aspirational.

⚡ Your mission: Help us tell the world about the first device that can improve memory while you sleep—with ads so compelling people can’t scroll past.

```html
<!DOCTYPE html>
<html lang="en">
<head>
<meta charset="utf-8">
<title>Quillbright — Social Ads</title>
<link href="https://fonts.googleapis.com/css2?family=Outfit:wght@300;400;500;600&display=swap" rel="stylesheet">
<style>
  :root {
    --canvas-bg: #c5d0ea;
    --ad-top: #2c4178;
    --ad-mid: #4a6ea9;
    --ad-bottom: #8174b3;
    --wave: #8fb0e0;
    --device-light: #f7f7f8;
    --device-shade: #d9dbe0;
    --copper: #d98a63;
    --button: #1f3370;
    --text: #ffffff;
  }
  * { box-sizing: border-box; margin: 0; padding: 0; }
  html, body {
    width: 1200px; height: 1000px; overflow: hidden;
    background: var(--canvas-bg);
    font-family: "Outfit", sans-serif;
    color: var(--text);
  }
  .stage { position: relative; width: 1200px; height: 1000px; }

  .ad {
    position: absolute;
    width: 416px;
    background: linear-gradient(180deg, var(--ad-top) 0%, var(--ad-mid) 45%, var(--ad-bottom) 100%);
    overflow: hidden;
  }
  .ad--square { left: 143px; top: 292px; height: 416px; }
  .ad--story { left: 641px; top: 130px; height: 740px; }

  .ad__brand {
    position: absolute; left: 0; right: 0;
    display: flex; align-items: center; justify-content: center; gap: 8px;
    font-weight: 300; letter-spacing: 0.06em;
  }
  .ad__brand-dot {
    width: 8px; height: 8px; border-radius: 50%;
    background: var(--text);
  }
  .ad--square .ad__brand { top: 30px; font-size: 21px; }
  .ad--story .ad__brand { top: 100px; font-size: 26px; }

  .ad__headline {
    position: absolute; left: 0; right: 0;
    text-align: center; font-weight: 600;
    font-size: 36px; line-height: 37px; letter-spacing: -0.005em;
  }
  .ad--square .ad__headline { top: 65px; }
  .ad--story .ad__headline { top: 151px; }

  .ad__airflow {
    position: absolute; left: 0; right: 0;
    background: radial-gradient(ellipse at center, rgba(143,176,224,0.55) 0%, rgba(143,176,224,0.25) 45%, rgba(143,176,224,0) 75%);
  }
  .ad--square .ad__airflow { top: 170px; height: 130px; }
  .ad--story .ad__airflow { top: 320px; height: 190px; }

  .ad__device {
    position: absolute;
    border-radius: 4px 4px 14px 14px;
    background: linear-gradient(90deg, var(--device-light) 0%, #ffffff 50%, var(--device-shade) 100%);
    box-shadow: 0 10px 18px rgba(20, 30, 70, 0.35);
  }
  .ad__device::after {
    content: ""; position: absolute; left: 0; right: 0; bottom: 0; height: 6px;
    border-radius: 0 0 14px 14px; background: var(--copper);
  }
  .ad--square .ad__device { left: 155px; top: 154px; width: 105px; height: 157px; }
  .ad--story .ad__device { left: 114px; top: 253px; width: 184px; height: 280px; }

  .ad__benefits {
    position: absolute; left: 0; right: 0;
    text-align: center; font-weight: 600; white-space: nowrap;
  }
  .ad__benefits .sep { margin: 0 6px; font-weight: 400; }
  .ad--square .ad__benefits { top: 322px; font-size: 13px; }
  .ad--story .ad__benefits { top: 556px; font-size: 16px; }

  .ad__cta {
    position: absolute; left: 50%; transform: translateX(-50%);
    display: flex; align-items: center; justify-content: center;
    background: var(--button); border-radius: 999px;
    font-weight: 400; white-space: nowrap;
  }
  .ad__cta sup { font-size: 0.6em; margin-left: 1px; }
  .ad--square .ad__cta { top: 349px; width: 160px; height: 28px; font-size: 11.5px; }
  .ad--story .ad__cta { top: 589px; width: 188px; height: 34px; font-size: 13px; }

  .ad__url {
    position: absolute; left: 0; right: 0;
    text-align: center; font-weight: 400; letter-spacing: 0.02em;
  }
  .ad--square .ad__url { top: 386px; font-size: 10.5px; }
  .ad--story .ad__url { top: 632px; font-size: 12px; }
</style>
</head>
<body>
<main class="stage">

  <section class="ad ad--square" aria-label="Quillbright square feed ad">
    <div class="ad__brand"><span class="ad__brand-dot"></span>Quillbright</div>
    <h1 class="ad__headline">Improve Memory<br>While You Sleep</h1>
    <div class="ad__airflow" role="img" aria-label="Soft flowing air waves spreading from the device"></div>
    <div class="ad__device" role="img" aria-label="White Quillbright bedside scent device with copper trim"></div>
    <p class="ad__benefits">Clinically Backed<span class="sep">·</span>Drug-Free<span class="sep">·</span>Effortless</p>
    <div class="ad__cta">Explore Quillbright<sup>TM</sup></div>
    <p class="ad__url">www.quillbright-example.com</p>
  </section>

  <section class="ad ad--story" aria-label="Quillbright story ad">
    <div class="ad__brand"><span class="ad__brand-dot"></span>Quillbright</div>
    <h1 class="ad__headline">Improve Memory<br>While You Sleep</h1>
    <div class="ad__airflow" role="img" aria-label="Soft flowing air waves spreading from the device"></div>
    <div class="ad__device" role="img" aria-label="White Quillbright bedside scent device with copper trim"></div>
    <p class="ad__benefits">Clinically Backed<span class="sep">·</span>Drug-Free<span class="sep">·</span>Effortless</p>
    <div class="ad__cta">Explore Quillbright<sup>TM</sup></div>
    <p class="ad__url">www.quillbright-example.com</p>
  </section>

</main>
</body>
</html>
```